Financial industry/Advisor business card

I'm a Financial Advisor starting my own investment company, Brandvik Wealth Management. I currently use the 'Light Blue' color that's provided on the Cardmello web page, but I want something unique. I'd like to keep the color, but the design is up for grabs.

Industry/Entity Type

Business

Contact Information for Business Card

Brandvik Wealth Management
Dale R. Brandvik
President
5142 Gableston Ln
Ste 240
Chadds Ford Pa 19402
610-555-0147-Office
610-555-0183-Fax
DBRANDVIK@BRANDVIKW.example

```html
<!DOCTYPE html>
<html lang="en">
<head>
<meta charset="utf-8">
<title>Brandvik Wealth Management – Business Card</title>
<link rel="stylesheet" href="https://fonts.googleapis.com/css2?family=Marcellus+SC&display=swap">
<style>
  :root {
    --card-black: #0b0d0e;
    --monogram-tone: #1b2222;
    --accent-cyan: #5fe9f5;
    --type-white: #f4f6f6;
    --type-soft: #c9d3d4;
    --edge-white: #e9eef0;
  }
  * { margin: 0; padding: 0; box-sizing: border-box; }
  html, body {
    width: 1200px;
    height: 704px;
    overflow: hidden;
    background: var(--card-black);
  }
  .card {
    position: relative;
    width: 1200px;
    height: 704px;
    background: var(--card-black);
    font-family: "Marcellus SC", serif;
    color: var(--type-white);
    overflow: hidden;
  }
  .monogram-backdrop {
    position: absolute;
    left: 0;
    top: 40px;
    width: 1180px;
    height: 600px;
    background: radial-gradient(ellipse at 30% 50%, var(--monogram-tone) 0%, rgba(27,34,34,0.35) 45%, transparent 70%),
                radial-gradient(ellipse at 80% 55%, var(--monogram-tone) 0%, rgba(27,34,34,0.35) 45%, transparent 70%);
    opacity: 0.8;
  }
  .brand-mark {
    position: absolute;
    left: 0;
    right: 0;
    top: 120px;
    display: flex;
    justify-content: center;
    align-items: center;
    gap: 16px;
    font-size: 46px;
    line-height: 1;
    letter-spacing: 2px;
    color: var(--accent-cyan);
  }
  .brand-mark-square {
    width: 22px;
    height: 22px;
    background: var(--accent-cyan);
  }
  .company-line {
    position: absolute;
    left: 0;
    right: 0;
    top: 316px;
    text-align: center;
    font-size: 60px;
    line-height: 1;
    white-space: nowrap;
    letter-spacing: 1px;
  }
  .contact-block {
    position: absolute;
    left: 0;
    right: 0;
    top: 428px;
    text-align: center;
    font-size: 24px;
    line-height: 1.6;
    letter-spacing: 1px;
    color: var(--type-soft);
    white-space: nowrap;
  }
  .contact-sep { color: var(--accent-cyan); padding: 0 10px; }
  .person-title,
  .person-name {
    position: absolute;
    top: 626px;
    font-size: 42px;
    line-height: 1;
    white-space: nowrap;
  }
  .person-title { left: 46px; }
  .person-name { right: 46px; }
  .edge-notch {
    position: absolute;
    top: 578px;
    width: 36px;
    height: 124px;
  }
  .edge-notch--left { left: 0; }
  .edge-notch--right { right: 0; }
  .edge-notch polygon {
    fill: var(--accent-cyan);
    stroke: var(--edge-white);
    stroke-width: 4;
  }
</style>
</head>
<body>
  <div class="card">
    <div class="monogram-backdrop" role="img" aria-label="Large faint monogram letters as background decoration"></div>

    <div class="brand-mark">
      <span class="brand-mark-square"></span>
      <span class="brand-mark-name">Brandvik</span>
    </div>

    <div class="company-line">Brandvik Wealth Management</div>

    <div class="contact-block">
      <p class="contact-address">5142 Gableston Ln<span class="contact-sep">·</span>Ste 240<span class="contact-sep">·</span>Chadds Ford Pa 19402</p>
      <p class="contact-phones">610-555-0147 Office<span class="contact-sep">·</span>610-555-0183 Fax</p>
      <p class="contact-email">DBRANDVIK@BRANDVIKW.example</p>
    </div>

    <div class="person-title">President</div>
    <div class="person-name">Dale R. Brandvik</div>

    <svg class="edge-notch edge-notch--left" viewBox="0 0 36 124" aria-hidden="true">
      <polygon points="-4,2 32,62 -4,122"/>
    </svg>
    <svg class="edge-notch edge-notch--right" viewBox="0 0 36 124" aria-hidden="true">
      <polygon points="40,2 4,62 40,122"/>
    </svg>
  </div>
</body>
</html>
```